Vantrel Ashcombe LLC

we need a business card design

Industry/Entity Type

hvac

Contact Information for Business Card

my logo

Requirements
Must have
• my logo and same colors

```html
<!DOCTYPE html>
<html lang="en">
<head>
<meta charset="utf-8">
<title>Vantrel Ashcombe LLC – Business Card</title>
<link href="https://fonts.googleapis.com/css2?family=Inter:wght@400;500;600;700&display=swap" rel="stylesheet">
<style>
  :root {
    --page-bg: #e0e0e0;
    --charcoal: #414141;
    --brand-blue: #0f56a3;
    --brand-orange: #f9b44c;
    --text-grey: #5c5c5c;
    --white: #ffffff;
  }
  * { margin: 0; padding: 0; box-sizing: border-box; }
  html, body {
    width: 1200px; height: 1200px; overflow: hidden;
    background: var(--page-bg);
    font-family: "Inter", Arial, sans-serif;
  }
  .card {
    position: absolute;
    left: 179px;
    width: 861px;
    height: 496px;
    overflow: hidden;
  }
  .card-front { top: 84px; background: var(--charcoal); }
  .card-back { top: 621px; background: var(--white); }

  .brand-lockup {
    position: absolute;
    display: flex; align-items: center; gap: 14px;
    transform: translate(-50%, -50%);
    white-space: nowrap;
    font-weight: 700;
  }
  .brand-mark {
    width: 30px; height: 30px; border-radius: 50%;
    background: var(--brand-orange);
  }
  .card-front .brand-lockup { left: 430px; top: 251px; }
  .card-front .brand-name { color: var(--white); font-size: 36px; }
  .card-back .brand-lockup { left: 640px; top: 300px; }
  .card-back .brand-name { color: var(--brand-blue); font-size: 26px; }

  .person { position: absolute; left: 40px; top: 72px; }
  .person-name {
    color: var(--brand-blue); font-weight: 600;
    font-size: 31px; letter-spacing: 1px; line-height: 1.1;
  }
  .person-title {
    color: var(--text-grey); font-size: 25px; letter-spacing: 1px;
    margin-top: 4px;
  }
  .title-rule {
    width: 84px; height: 4px; background: var(--brand-orange);
    margin-top: 6px;
  }
  .address {
    position: absolute; left: 38px; top: 195px;
    color: var(--text-grey); font-size: 21px; font-weight: 500;
    letter-spacing: 3px; line-height: 34px;
  }
  .contacts {
    position: absolute; left: 36px; top: 297px;
    list-style: none;
  }
  .contacts li {
    display: flex; align-items: center; gap: 14px;
    height: 37px;
    color: var(--text-grey); font-size: 21px; font-weight: 500;
    letter-spacing: 3px;
  }
  .contacts svg { width: 24px; height: 24px; flex: none; }
  .wave { position: absolute; left: 0; top: 0; width: 861px; height: 496px; }
</style>
</head>
<body>

<section class="card card-front">
  <div class="brand-lockup">
    <span class="brand-mark"></span>
    <span class="brand-name">Vantrel Ashcombe LLC</span>
  </div>
</section>

<section class="card card-back">
  <svg class="wave" viewBox="0 0 861 496" aria-hidden="true">
    <path d="M0 422 C 200 460, 420 430, 600 392 C 720 366, 800 365, 861 372 L861 496 L0 496 Z" fill="var(--charcoal)"/>
    <path d="M0 422 C 200 460, 420 430, 600 392 C 720 366, 800 365, 861 372" fill="none" stroke="var(--brand-orange)" stroke-width="9"/>
  </svg>

  <div class="person">
    <h1 class="person-name">DORIAN KESSEL</h1>
    <p class="person-title">DIRECTOR</p>
    <div class="title-rule"></div>
  </div>

  <p class="address">Anywhere St.<br>Any City, ST 123</p>

  <ul class="contacts">
    <li>
      <svg viewBox="0 0 24 24"><path d="M6.6 10.8a15 15 0 0 0 6.6 6.6l2.2-2.2a1 1 0 0 1 1-.25 11.4 11.4 0 0 0 3.6.57 1 1 0 0 1 1 1V20a1 1 0 0 1-1 1A17 17 0 0 1 3 4a1 1 0 0 1 1-1h3.5a1 1 0 0 1 1 1c0 1.25.2 2.45.57 3.57a1 1 0 0 1-.25 1z" fill="var(--brand-blue)"/></svg>
      <span>800-222-2222</span>
    </li>
    <li>
      <svg viewBox="0 0 24 24"><rect x="2" y="5" width="20" height="14" fill="var(--brand-blue)"/><path d="M2 5l10 8 10-8" fill="none" stroke="var(--white)" stroke-width="1.6"/></svg>
      <span>email@yoursite.com</span>
    </li>
    <li>
      <svg viewBox="0 0 24 24" fill="none" stroke="var(--brand-blue)" stroke-width="1.8"><circle cx="12" cy="12" r="10" fill="var(--brand-blue)"/><path d="M2 12h20M12 2c3 3 3 17 0 20M12 2c-3 3-3 17 0 20M4 7h16M4 17h16" stroke="var(--white)" stroke-width="1.2"/></svg>
      <span>www.yoursite.com</span>
    </li>
  </ul>

  <div class="brand-lockup">
    <span class="brand-mark"></span>
    <span class="brand-name">Vantrel Ashcombe LLC</span>
  </div>
</section>

</body>
</html>
```